Advertisement flyer for fire sprinkler repair parts. The projected audience are contractors.

I need a flyer advertising specific parts that we are stocking at our company "Meridian Valvecraft Supply." I have attached a picture of our logo. I want the title to say "Fire Pump Repair Parts and Accessories." I want to specifically advertise the following parts: Repack Kits and Repair Parts, Jockey Pumps, Pump Controllers, Casing Relief Valves, Air Release Valves, Suction/Discharge Gauges, Pump Shaft Couplers & Shim Kits, Fire Pump Relief Valves, and QN Listed Pressure Reducing Valves. I have attached pictures of the manufacturers I want to advertise on this flyer. I have also attached pictures of some of the parts we are stocking that I would like to be included somewhere in the flyer. I would like all of the pictures to have a transparent background. Also I would like our phone number :(800)-431-2867, and our website www.tolvenspares.example included. I made my own design that I have Attached. You do not have to go based off this design, but I would like the basic content to be the same. We do have Same- Day shipping as well as Free Tech Support if you can include that anywhere.

```html
<!DOCTYPE html>
<html lang="en">
<head>
<meta charset="utf-8">
<title>Meridian Valvecraft Supply – Fire Pump Repair Parts Flyer</title>
<link rel="stylesheet" href="https://fonts.googleapis.com/css2?family=Arimo:wght@400;700&display=swap">
<style>
  :root{
    --page-bg:#9a9a9a;
    --white:#ffffff;
    --brand-blue:#3049a0;
    --brand-red:#e8203a;
    --ink-black:#111111;
    --photo-red:#a8302c;
    --photo-grey:#b9b4ae;
    --panel-grey:#cfcac4;
    --logo-ink:#23336f;
  }
  *{margin:0;padding:0;box-sizing:border-box;}
  html,body{width:1200px;height:2250px;overflow:hidden;}
  body{background:var(--page-bg);font-family:"Arimo",Arial,sans-serif;position:relative;}
  .flyer{position:absolute;left:50px;top:414px;width:1100px;height:1422px;background:var(--white);overflow:hidden;box-shadow:0 14px 30px rgba(0,0,0,.45);}
  .hero-photo{position:absolute;left:0;top:0;width:1100px;height:560px;
    background:linear-gradient(160deg,#d8d2cc 0%,#b24a42 30%,var(--photo-red) 55%,#7d6a62 80%,#c9c2ba 100%);}
  .header-shape{position:absolute;left:0;top:0;}
  .brand{position:absolute;left:38px;top:50px;display:flex;align-items:center;gap:18px;}
  .brand-mark{width:52px;height:52px;background:var(--brand-red);}
  .brand-name{color:var(--brand-blue);font-weight:400;font-size:38px;line-height:1;}
  .divider{position:absolute;left:0;top:500px;}
  .parts-panel{position:absolute;left:0;top:570px;width:593px;height:593px;background:var(--brand-red);padding:30px 0 0 40px;color:var(--white);overflow:hidden;}
  .parts-title{font-weight:700;font-size:40px;line-height:45px;margin-bottom:32px;}
  .parts-list{list-style:none;}
  .parts-list li{font-size:24px;line-height:42.3px;height:42.3px;display:flex;align-items:center;white-space:nowrap;}
  .parts-list li::before{content:"";width:12px;height:12px;background:rgba(255,255,255,.8);margin-right:26px;flex:none;}
  .product-panel{position:absolute;left:593px;top:537px;width:507px;height:626px;
    background:linear-gradient(180deg,#e4e0dc 0%,var(--panel-grey) 50%,#aaa39b 100%);}
  .product-shot{position:absolute;width:224px;height:224px;border-radius:50%;border:4px solid var(--ink-black);
    background:radial-gradient(circle,#ffffff 40%,#ececec 100%);}
  .contact-band{position:absolute;left:0;top:1163px;width:1100px;height:156px;}
  .contact-band svg{position:absolute;left:0;top:0;}
  .call-line{position:absolute;left:42px;top:26px;color:var(--white);font-weight:700;font-size:58px;line-height:1;}
  .web-line{position:absolute;left:42px;top:100px;color:var(--white);font-size:38px;line-height:1;}
  .maker-row{position:absolute;left:0;top:1319px;width:1100px;height:103px;display:flex;align-items:center;justify-content:space-between;padding:0 26px;}
  .maker{color:var(--logo-ink);font-weight:700;font-size:21px;}
</style>
</head>
<body>
  <main class="flyer">
    <div class="hero-photo" role="img" aria-label="Photo of a fire pump room with red-painted pipes, valves and pumps"></div>

    <svg class="header-shape" width="1100" height="175" viewBox="0 0 1100 175">
      <polygon points="0,0 640,0 568,161 0,161" fill="var(--white)"/>
      <polygon points="640,0 660,0 584,175 0,175 0,161 568,161" fill="var(--brand-blue)"/>
    </svg>
    <div class="brand">
      <span class="brand-mark"></span>
      <span class="brand-name">Meridian Valvecraft Supply</span>
    </div>

    <div class="product-panel" role="img" aria-label="Faded photo of pump room piping behind product images">
      <div class="product-shot" style="left:17px;top:67px" role="img" aria-label="Pressure reducing valve"></div>
      <div class="product-shot" style="left:263px;top:67px" role="img" aria-label="Red fire pump assembly"></div>
      <div class="product-shot" style="left:17px;top:355px" role="img" aria-label="Vertical jockey pump"></div>
      <div class="product-shot" style="left:263px;top:355px" role="img" aria-label="Pump shaft couplers and shim kit"></div>
    </div>

    <svg class="divider" width="1100" height="70" viewBox="0 0 1100 70">
      <polygon points="0,52 400,52 428,20 1100,20 1100,37 436,37 408,70 0,70" fill="var(--brand-blue)"/>
    </svg>

    <section class="parts-panel">
      <h1 class="parts-title">Fire Pump Repair Parts &amp;<br>Accessories!</h1>
      <ul class="parts-list">
        <li>Fire Pump Repack Kits</li>
        <li>Jockey Pumps</li>
        <li>Pump Controllers</li>
        <li>Casing Relief Valves</li>
        <li>Air Release Valves</li>
        <li>Suction / Discharge Gauges</li>
        <li>Flow Meters</li>
        <li>Pump Shaft Couplers &amp; Shim Kits</li>
        <li>Fire Pump Relief Valves</li>
        <li>QN Listed Pressure Reducing Valves</li>
      </ul>
    </section>

    <section class="contact-band">
      <svg width="1100" height="156" viewBox="0 0 1100 156">
        <polygon points="0,0 990,0 1050,156 0,156" fill="var(--brand-blue)"/>
        <polygon points="1026,0 1062,0 1100,98 1100,156 1086,156" fill="var(--ink-black)"/>
      </svg>
      <p class="call-line">Call Us Today: (800) 431-2867</p>
      <p class="web-line">visit us www.tolvenspares.example</p>
    </section>

    <footer class="maker-row">
      <span class="maker">Halvern</span>
      <span class="maker">Brightmoor</span>
      <span class="maker">Kestrel</span>
      <span class="maker">Dunmore</span>
      <span class="maker">Ostrava</span>
      <span class="maker">Pellwick</span>
      <span class="maker">Quarryline</span>
      <span class="maker">Tessaly</span>
    </footer>
  </main>
</body>
</html>
```